Emergency Medical Training and Events Company Business Needs Business Card Design

We are in need of a business card for our dynamic company expanding its customer base and need to be easily contacted and identified for when we visit with government officials, potential EMS / Fire agencies and county coordinators to arrange for training programs for first responders to better prepare them for critical thinking at critical incidents.
Updates

Need extra days to review

Target Market(s)

EMS/Fire and Event Promoters

Industry/Entity Type

Medical

Contact Information for Business Card

Two cards, comparable designs:

Gavin R. Thorley, Principal, g.thorley@vantrexmed.com
Neil Carrow, Event and Training Specialist, n.carrow@vantrexmed.com

Font styles to use
Other font styles liked:
• Cambria

Colors

Designer to choose colors to be used in the design.

Requirements
Must have
• Company Logo, Spots for Name, Title, Phone Number, Email, Website
• A bullet list stating that we offer, KMB CPR and First Aid Instructors, Hold the Line Instructors, Event EMS, CME's, MCI Training and Planning. We prefer to have a black background for the card but if you can make a blue or white card stand out we would review that as well.
Should not have
• Tacky logos or special sayings ... simple, elegant, professional is the look we seek

```html
<!DOCTYPE html>
<html lang="en">
<head>
<meta charset="utf-8">
<title>Vantrex Medical – Stationery</title>
<link href="https://fonts.googleapis.com/css2?family=Lato:wght@400;700&family=Roboto:wght@400&family=Roboto+Condensed:wght@400&display=swap" rel="stylesheet">
<style>
  :root {
    --navy: #1e1d4c;
    --red: #c4202b;
    --red-soft: #b72a36;
    --white: #ffffff;
    --ink: #555555;
    --backdrop: #dcdcdc;
  }
  * { margin: 0; padding: 0; box-sizing: border-box; }
  html, body { width: 1200px; height: 1200px; overflow: hidden; }
  body { background: var(--backdrop); position: relative; font-family: "Lato", sans-serif; }

  .letterhead { position: absolute; left: 40px; top: 179px; width: 595px; height: 842px; background: var(--white); overflow: hidden; }
  .letterhead__wash { position: absolute; inset: 0; background: linear-gradient(159deg, var(--navy) 0px, rgba(30,29,76,.55) 45px, rgba(255,255,255,0) 140px); }
  .letterhead__brand { position: absolute; left: 9px; top: 11px; }
  .letterhead__rule { position: absolute; left: 9px; top: 57px; width: 578px; height: 2px; background: linear-gradient(90deg, var(--white) 0 105px, var(--red) 105px); }
  .letterhead__contact { position: absolute; left: 428px; top: 6px; font-family: "Roboto", sans-serif; font-size: 11.5px; color: var(--ink); line-height: 15.5px; white-space: nowrap; }
  .letterhead__contact li { list-style: none; display: flex; align-items: center; gap: 6px; }
  .letterhead__contact .accent { color: var(--red); }
  .letterhead__footer { position: absolute; left: 0; bottom: 0; width: 595px; height: 45px; }
  .letterhead__address { position: absolute; left: 0; right: 40px; bottom: 6px; text-align: center; color: var(--white); font-size: 15px; }

  .brand { display: flex; align-items: center; gap: 6px; color: var(--white); font-family: "Lato", sans-serif; font-weight: 700; letter-spacing: .5px; white-space: nowrap; line-height: 1.05; }
  .brand__dot { border-radius: 50%; background: var(--white); flex: none; }
  .letterhead__brand { font-size: 13px; }
  .letterhead__brand .brand__dot { width: 32px; height: 32px; }

  .card { position: absolute; left: 661px; width: 500px; height: 286px; background: var(--navy); overflow: hidden; color: var(--white); }
  .card--front { top: 274px; }
  .card--back { top: 628px; }
  .card .brand { position: absolute; font-size: 18px; gap: 8px; }
  .card .brand__dot { width: 44px; height: 44px; }
  .card--front .brand { left: 78px; top: 108px; }
  .card--back .brand { left: 60px; top: 106px; }
  .card__wave { position: absolute; left: 0; bottom: 0; width: 500px; height: 33px; }

  .person { position: absolute; left: 263px; top: 55px; border-left: 1.5px solid var(--white); padding-left: 5px; font-family: "Roboto Condensed", sans-serif; }
  .person__name { font-size: 18px; line-height: 18px; letter-spacing: -.3px; }
  .person__name .accent { color: var(--red); }
  .person__title { font-size: 13.5px; margin-top: 6px; }
  .details { position: absolute; left: 263px; top: 114px; height: 87px; border-left: 1.5px solid var(--red); padding-left: 6px; font-family: "Roboto", sans-serif; font-size: 12.5px; line-height: 16px; }
  .details__list { margin-top: 9px; }
  .details__list li { list-style: none; display: flex; align-items: center; gap: 9px; line-height: 18px; }

  .offer { position: absolute; left: 250px; top: 83px; height: 86px; border-left: 2px solid var(--white); padding-left: 26px; }
  .offer__heading { color: var(--red); font-size: 16px; line-height: 16px; margin-top: -4px; }
  .offer__list li { list-style: none; font-size: 13.5px; line-height: 19.3px; }
  .card__web { position: absolute; left: 16px; bottom: 14px; display: flex; align-items: center; gap: 8px; font-family: "Roboto", sans-serif; font-size: 15px; }
</style>
</head>
<body>

<section class="letterhead">
  <div class="letterhead__wash"></div>
  <div class="brand letterhead__brand"><span class="brand__dot"></span><span>VANTREX<br>MEDICAL</span></div>
  <ul class="letterhead__contact">
    <li><svg width="8" height="8" viewBox="0 0 10 10"><path d="M2 1l2 2-1 1.5a6 6 0 003 3L7.5 6l2 2-1.5 1.5C4 9 1 6 .5 2.5z" fill="#c4202b"/></svg><span>555 014 2290</span></li>
    <li><svg width="8" height="6" viewBox="0 0 10 7"><rect width="10" height="7" fill="#c4202b"/><path d="M0 0l5 4 5-4" stroke="#fff" fill="none"/></svg><span>g.thorley@<span class="accent">vantrexmed</span>.com</span></li>
    <li><svg width="8" height="8" viewBox="0 0 10 10" fill="none" stroke="#c4202b"><circle cx="5" cy="5" r="4.3"/><path d="M.7 5h8.6M5 .7c-2.5 2.7-2.5 5.9 0 8.6M5 .7c2.5 2.7 2.5 5.9 0 8.6"/></svg><span>www.<span class="accent">vantrexmed</span>.com</span></li>
  </ul>
  <div class="letterhead__rule"></div>
  <svg class="letterhead__footer" viewBox="0 0 595 45" preserveAspectRatio="none">
    <path d="M0 6H372C378 6 380 11 374 15H0Z" fill="#1e1d4c"/>
    <path d="M0 19H372C388 19 392 0 412 0H595V45H0Z" fill="#b72a36"/>
  </svg>
  <p class="letterhead__address">PO Box 218 Carvale, New York, USA</p>
</section>

<section class="card card--front">
  <div class="brand"><span class="brand__dot"></span><span>VANTREX<br>MEDICAL</span></div>
  <div class="person">
    <p class="person__name"><span class="accent">GAVIN R</span>. THORLEY</p>
    <p class="person__title">Principal</p>
  </div>
  <div class="details">
    <p>PO Box 218 Carvale,<br>New York, USA</p>
    <ul class="details__list">
      <li><svg width="6" height="10" viewBox="0 0 6 10"><rect x=".6" y=".6" width="4.8" height="8.8" rx="1" fill="none" stroke="#c4202b" stroke-width="1.2"/></svg><span>555 014 2290</span></li>
      <li><svg width="9" height="6" viewBox="0 0 10 7"><rect width="10" height="7" fill="#c4202b"/><path d="M0 0l5 4 5-4" stroke="#1e1d4c" fill="none"/></svg><span>g.thorley@vantrexmed.com</span></li>
      <li><svg width="9" height="9" viewBox="0 0 10 10" fill="none" stroke="#c4202b"><circle cx="5" cy="5" r="4.3"/><path d="M.7 5h8.6M5 .7c-2.5 2.7-2.5 5.9 0 8.6M5 .7c2.5 2.7 2.5 5.9 0 8.6"/></svg><span>www.vantrexmed.com</span></li>
    </ul>
  </div>
  <svg class="card__wave" viewBox="0 0 500 33" preserveAspectRatio="none">
    <path d="M0 4H318C324 4 326 9 320 13H0Z" fill="#fff"/>
    <path d="M0 16H316C330 16 334 0 350 0H500V33H0Z" fill="#c4202b"/>
  </svg>
</section>

<section class="card card--back">
  <div class="brand"><span class="brand__dot"></span><span>VANTREX<br>MEDICAL</span></div>
  <div class="offer">
    <p class="offer__heading">We Offer</p>
    <ul class="offer__list">
      <li>Training Planning</li>
      <li>CPR/AED Training</li>
      <li>First Aid Training</li>
      <li>EMS Event Management</li>
    </ul>
  </div>
  <svg class="card__wave" viewBox="0 0 500 33" preserveAspectRatio="none">
    <path d="M185 4H500V13H192C184 13 180 4 185 4Z" fill="#fff"/>
    <path d="M0 0H168C180 0 184 16 196 16H500V33H0Z" fill="#c4202b"/>
  </svg>
  <p class="card__web"><svg width="10" height="10" viewBox="0 0 10 10" fill="none" stroke="#fff"><circle cx="5" cy="5" r="4.3"/><path d="M.7 5h8.6M5 .7c-2.5 2.7-2.5 5.9 0 8.6M5 .7c2.5 2.7 2.5 5.9 0 8.6"/></svg><span>www.vantrexmed.com</span></p>
</section>

</body>
</html>
```